3月15日にガールズバーをオープン致しました。
ビルの入り口に置いて使うA1立て看板の製作をお願いします。
A4など縮小サイズでもいただけると助かります。
白を基調とした夜でも目立つ感じにしたいです。

セット料金 40分2000円 tax&service 20%

チャージのみ1時間1500円 tax&service 15

クレジットチャージ 10%
飲み放題付き (焼酎 ウイスキー カクテルなど)
ビル3階 席数17席  団体客歓迎

若いギャル系の女の子の写真を大きく入れて頂きたいのですが素材が無く
困ってます。素材をお持ちかたにお願いしたいと思ってます。

現在の看板を添付致しました。ご参考までに。
文章は記載しないでも大丈夫です。

店舗名 Sunflower(サンフラワー)です。

よろしくお願いします。
資料を再添付致しました。よろしくお願いします。
依頼金額を25000円に変更して、延長しました。
提案下さった皆様ありがとうございます。
もう少し提案を見させていただけたらと思います。

具体的なイメージをデザベース様の過去の事例で近いものを添付致しました。
よろしくお願いします。

最初に思い描いてたイメージより良かったです
女の子と背景のピンクもかわいいくて満足です。

ありがとうございました!

提案くださった皆様ありがとうございます!
修正をしてくださった皆様も早急な対応に感謝致します。

ありがとうございました!

```html
<!DOCTYPE html>
<html lang="ja">
<head>
<meta charset="utf-8">
<title>Girl's Bar Sunflower</title>
<link href="https://fonts.googleapis.com/css2?family=Great+Vibes&family=Playfair+Display:wght@700;900&family=Noto+Sans+JP:wght@500;700;900&family=Noto+Serif+JP:wght@700;900&display=swap" rel="stylesheet">
<style>
  :root{
    --magenta:#d1145a;
    --magenta-dark:#a80d47;
    --gold:#b08a4e;
    --gray:#8d8d8d;
    --ink:#333;
    --white:#ffffff;
    --photo-light:#f3e6dc;
    --photo-mid:#e6c9b4;
    --photo-dark:#c9a58c;
  }
  *{margin:0;padding:0;box-sizing:border-box;}
  html,body{width:848px;height:1200px;overflow:hidden;background:var(--white);}
  .board{position:relative;width:848px;height:1200px;background:var(--white);overflow:hidden;font-family:"Noto Sans JP",sans-serif;color:var(--ink);}

  .tagline{position:absolute;top:14px;left:0;width:100%;text-align:center;font-family:"Noto Sans JP",sans-serif;font-weight:900;font-size:44px;color:var(--magenta);letter-spacing:1px;}
  .tagline-rule{position:absolute;top:84px;left:0;width:100%;height:4px;background:var(--magenta);}

  .model-photo{position:absolute;top:88px;left:400px;width:448px;height:1112px;
    background:linear-gradient(160deg,var(--photo-light) 0%,var(--photo-mid) 55%,var(--photo-dark) 100%);}

  .brand{position:absolute;top:170px;left:30px;width:410px;text-align:center;}
  .brand-kind{font-family:"Great Vibes",cursive;font-size:48px;color:var(--magenta);line-height:1;}
  .brand-name{font-family:"Playfair Display",serif;font-weight:900;font-size:86px;color:var(--magenta);line-height:1.05;}
  .brand-kana{display:flex;align-items:center;justify-content:center;gap:10px;font-size:20px;font-weight:700;color:var(--magenta);}
  .brand-kana::before,.brand-kana::after{content:"";width:70px;height:2px;background:var(--magenta);}

  .price{position:absolute;left:40px;padding-left:30px;}
  .price::before{content:"";position:absolute;left:0;top:6px;bottom:6px;width:14px;}
  .price-set{top:410px;color:var(--gold);}
  .price-set::before{background:var(--gold);}
  .price-charge{top:612px;color:var(--gray);}
  .price-charge::before{background:var(--gray);}
  .price-label{font-family:"Playfair Display",serif;font-weight:700;font-size:40px;line-height:1;letter-spacing:2px;}
  .price-amount{font-family:"Playfair Display",serif;font-weight:900;font-size:108px;line-height:1;}
  .price-amount .yen{font-family:"Noto Serif JP",serif;font-size:58px;margin-left:4px;}
  .price-note{font-size:24px;font-weight:500;color:var(--ink);margin-top:4px;}
  .per-hour{position:absolute;top:8px;left:400px;width:58px;height:58px;border-radius:50%;border:3px solid currentColor;background:var(--white);display:flex;flex-direction:column;align-items:center;justify-content:center;font-size:18px;font-weight:700;line-height:1.05;}

  .info-box{position:absolute;left:22px;top:900px;width:310px;height:288px;background:var(--magenta);color:var(--white);padding:18px 16px 0;font-weight:900;}
  .info-floor{font-size:46px;line-height:1.1;}
  .info-floor strong{font-size:80px;font-family:"Playfair Display",serif;}
  .info-seats{font-size:46px;line-height:1.15;}
  .info-group{font-size:40px;line-height:1.2;}
  .info-credit{position:absolute;left:0;bottom:0;width:100%;background:var(--magenta-dark);font-size:24px;padding:8px 16px;}

  .drinks{position:absolute;left:585px;top:960px;width:250px;height:210px;background:var(--white);border:5px solid var(--magenta);color:var(--magenta);text-align:center;padding-top:16px;font-weight:900;}
  .drinks-title{font-size:58px;line-height:1.05;}
  .drinks-list{font-size:18px;font-weight:700;margin-top:10px;}
</style>
</head>
<body>
<div class="board">
  <div class="tagline">シックでかわいいガールズバー</div>
  <div class="tagline-rule"></div>

  <div class="model-photo" role="img" aria-label="長い巻き髪の若い女性が白い花柄トップスで微笑む写真"></div>

  <div class="brand">
    <div class="brand-kind">Girl's Bar</div>
    <div class="brand-name">Sunflower</div>
    <div class="brand-kana">サンフラワー</div>
  </div>

  <div class="price price-set">
    <div class="price-label">SET</div>
    <div class="price-amount">3,000<span class="yen">円</span></div>
    <div class="price-note">tax &amp; service 20%</div>
    <div class="per-hour"><span>1</span><span>時間</span></div>
  </div>

  <div class="price price-charge">
    <div class="price-label">CHARGE</div>
    <div class="price-amount">1,500<span class="yen">円</span></div>
    <div class="price-note">tax &amp; service 15%</div>
    <div class="per-hour"><span>1</span><span>時間</span></div>
  </div>

  <div class="info-box">
    <div class="info-floor">当ビル <strong>3</strong>F</div>
    <div class="info-seats">席数17席</div>
    <div class="info-group">団体客歓迎!</div>
    <div class="info-credit">クレジットチャージ 10%</div>
  </div>

  <div class="drinks">
    <div class="drinks-title">飲み<br>放題付き</div>
    <div class="drinks-list">焼酎・ウイスキー・カクテルなど</div>
  </div>
</div>
</body>
</html>
```